UX Graphic design for a tablet - Commercial Vehicle Market

We need UX design for a 7"-10" tablet. We currently have a design for a mobile phone, but need a bigger design for tablet size.

We want to develop a landscape screen design for a 7”-10” tablet (needs to be compatible for both sizes). We have a current design that is (attached), but want to make some changes and come up with a better design. Maybe have the road temperature under the truck and the air temperature above the truck? We need it to be really easy to read as salt truck drivers look at these when they are plowing snow / putting salt on the roads.

Key requirements:
o Intuitive & easy to read display
o Air Temp
o Road Temp
o Truck on Road Graphic
o Truck Speed
o Plow Blade up/down
o Salt Spreader on/off
o Salt Spreading Rate
o Road Freeze Caution

```html
<!DOCTYPE html>
<html lang="en">
<head>
<meta charset="utf-8">
<title>FrostLine Tracker – Tablet Dashboard</title>
<link rel="stylesheet" href="https://fonts.googleapis.com/css2?family=Roboto:wght@300;400;500;700;900&display=swap">
<style>
  :root {
    --page-bg: #2a2c2f;
    --column-bg: #1b1c1e;
    --heading: #d7d9dc;
    --bar-black: #000000;
    --status-blue: #33b5e5;
    --btn-blue: #2f5f8f;
    --btn-grey: #555759;
    --btn-text: #e6eef6;
    --caution-red: #e0262c;
    --caution-text: #ff3b3b;
  }
  .mode-night {
    --sky: #2e5a86;
    --speed-tab: #1d3a5a;
    --ground: #2c2d2f;
    --ink: #ffffff;
    --label: #d9e4ef;
    --air-box: #5b93c9;
    --air-ink: #ffffff;
    --road-box: #e4e4e4;
    --road-ink: #3a3a3a;
    --more-btn: #4a4b4d;
    --logo-ink: #e8e8e8;
    --meta-ink: #c8c8c8;
    --truck-fill: #2b6cb0;
  }
  .mode-day {
    --sky: #a7d2f1;
    --speed-tab: #d4ecfb;
    --ground: #dcedf7;
    --ink: #1f3850;
    --label: #2c4660;
    --air-box: #d8ecfa;
    --air-ink: #2b5f93;
    --road-box: #f5f9fc;
    --road-ink: #2e4a66;
    --more-btn: #2f5f8f;
    --logo-ink: #1f3850;
    --meta-ink: #3c5670;
    --truck-fill: #2f78c4;
  }
  * { box-sizing: border-box; margin: 0; padding: 0; }
  html, body { width: 1200px; height: 1000px; overflow: hidden; }
  body {
    position: relative;
    background: var(--page-bg);
    font-family: "Roboto", Arial, sans-serif;
  }
  .mode-column {
    position: absolute; left: 0; top: 0;
    width: 356px; height: 1000px;
    background: var(--column-bg);
  }
  .mode-heading {
    position: absolute; left: 0; width: 342px;
    text-align: center;
    color: var(--heading);
    font-weight: 300; font-size: 24px; letter-spacing: 1px;
  }
  .screen-slot { position: absolute; }
  .screen-slot.thumb { left: 18px; width: 320px; height: 192px; }
  .screen-slot.thumb .screen { transform: scale(0.5); }
  .screen-slot.hero { left: 400px; top: 275px; width: 768px; height: 461px; }
  .screen-slot.hero .screen { transform: scale(1.2); }

  .screen {
    position: absolute; left: 0; top: 0;
    width: 640px; height: 384px;
    transform-origin: 0 0;
    background: var(--bar-black);
    overflow: hidden;
  }
  .status-bar {
    position: absolute; left: 0; top: 0; width: 640px; height: 20px;
    background: var(--bar-black);
    display: flex; justify-content: flex-end; align-items: center; gap: 5px;
    padding-right: 44px;
    color: var(--status-blue); font-size: 14px;
  }
  .status-bar svg { display: block; }
  .nav-column {
    position: absolute; right: 0; top: 20px; width: 40px; height: 364px;
    display: flex; flex-direction: column; justify-content: space-around; align-items: center;
    padding: 40px 0 60px;
  }
  .dashboard {
    position: absolute; left: 0; top: 20px; width: 600px; height: 324px;
    background: var(--ground);
    overflow: hidden;
  }
  .sky { position: absolute; left: 0; top: 0; width: 600px; height: 192px; background: var(--sky); }
  .speed-tab {
    position: absolute; left: -40px; top: -60px; width: 320px; height: 116px;
    background: var(--speed-tab);
    border-radius: 0 0 200px 0 / 0 0 70px 0;
  }
  .speed {
    position: absolute; left: 14px; top: 4px;
    display: flex; align-items: flex-start; color: var(--ink);
  }
  .speed .label { font-size: 11px; margin-top: 18px; margin-right: 8px; color: var(--label); }
  .speed .value { font-size: 44px; font-weight: 700; line-height: 48px; }
  .speed .unit { font-size: 13px; margin-left: 10px; margin-top: 6px; color: var(--label); }

  .readout-label { position: absolute; font-size: 11px; color: var(--label); text-transform: uppercase; }
  .temp-box {
    position: absolute; left: 456px; width: 124px; height: 56px;
    border-radius: 6px;
    display: flex; align-items: center; justify-content: center;
    font-size: 44px; font-weight: 700;
  }
  .temp-box .unit { position: absolute; right: 12px; top: 6px; font-size: 12px; font-weight: 400; }
  .air-temp { top: 32px; background: var(--air-box); color: var(--air-ink); }
  .air-label { left: 386px; top: 52px; }
  .road-temp { top: 240px; background: var(--road-box); color: var(--road-ink); }
  .road-temp.is-caution { background: var(--caution-red); color: #ffffff; }
  .road-label { left: 376px; top: 262px; }
  .caution-icon {
    position: absolute; left: 14px; top: 10px; width: 18px; height: 18px;
    border-radius: 50%; background: #ffffff; color: var(--caution-red);
    font-size: 14px; font-weight: 900; text-align: center; line-height: 18px;
  }
  .caution-note {
    position: absolute; left: 456px; top: 298px; width: 124px;
    text-align: center; font-size: 10px; color: var(--caution-text); letter-spacing: .5px;
  }

  .blade-state { position: absolute; left: 22px; top: 100px; color: var(--ink); text-align: left; }
  .blade-state .label { font-size: 13px; color: var(--label); }
  .blade-state .value { font-size: 28px; font-weight: 500; line-height: 30px; }
  .blade-state svg { display: block; margin-left: 18px; }
  .blade-state.is-up svg { margin-bottom: 2px; }

  .truck-graphic {
    position: absolute; left: 124px; top: 90px; width: 316px; height: 118px;
    background: linear-gradient(180deg, var(--truck-fill), #1f5a96);
    border-radius: 14px 30px 10px 10px;
    opacity: .9;
  }

  .spread-rate { position: absolute; left: 462px; top: 158px; display: flex; align-items: center; color: var(--ink); }
  .spread-rate .value { font-size: 30px; font-weight: 700; }
  .spread-rate .label { font-size: 11px; line-height: 11px; margin-left: 4px; text-align: right; color: var(--label); }

  .brand {
    position: absolute; left: 20px; top: 256px;
    display: flex; align-items: center; gap: 8px;
    font-size: 22px; font-weight: 500; color: var(--logo-ink);
  }
  .brand .dot { width: 14px; height: 14px; border-radius: 50%; background: var(--caution-red); }
  .app-meta { position: absolute; left: 20px; top: 306px; font-size: 8px; color: var(--meta-ink); }
  .more-button {
    position: absolute; left: 232px; top: 280px; width: 52px; height: 34px;
    background: var(--more-btn); color: #e6e6e6; border-radius: 2px;
    text-align: center; font-size: 14px; line-height: 30px;
  }
  .action-bar {
    position: absolute; left: 0; top: 344px; width: 600px; height: 40px;
    background: var(--bar-black);
  }
  .action-bar .btn {
    position: absolute; top: 4px; height: 32px;
    color: var(--btn-text); font-size: 15px; text-align: center; line-height: 32px;
  }
  .btn-settings { left: 128px; width: 116px; background: var(--btn-blue); }
  .btn-stop { left: 262px; width: 118px; background: var(--btn-grey); }
  .btn-quit { left: 396px; width: 118px; background: var(--btn-blue); }
</style>
</head>
<body>

<aside class="mode-column">
  <h2 class="mode-heading" style="top:50px">NIGHT MODE</h2>
  <h2 class="mode-heading" style="top:528px">DAY MODE</h2>
</aside>

<!-- Night – blade up -->
<div class="screen-slot thumb" style="top:84px">
  <div class="screen mode-night">
    <div class="status-bar">
      <svg width="12" height="12" viewBox="0 0 12 12"><circle cx="6" cy="6.5" r="4.5" fill="none" stroke="#33b5e5" stroke-width="1.4"/></svg>
      <svg width="14" height="12" viewBox="0 0 14 12"><path d="M1 4a9 9 0 0 1 12 0L7 11z" fill="#33b5e5"/></svg>
      <svg width="12" height="12" viewBox="0 0 12 12"><path d="M1 11h10V1z" fill="#33b5e5"/></svg>
      <svg width="7" height="12" viewBox="0 0 7 12"><rect x="0.5" y="1" width="6" height="10.5" fill="#33b5e5"/></svg>
      <span>13:37</span>
    </div>
    <div class="dashboard">
      <div class="sky"></div>
      <div class="speed-tab"></div>
      <div class="speed"><span class="label">SPEED</span><span class="value">24</span><span class="unit">MPH</span></div>
      <span class="readout-label air-label">Air Temp</span>
      <div class="temp-box air-temp">72<span class="unit">F</span></div>
      <div class="blade-state is-up">
        <svg width="14" height="8" viewBox="0 0 14 8"><path d="M1 7l6-6 6 6" fill="none" stroke="currentColor" stroke-width="2"/></svg>
        <div class="label">BLADE IS</div><div class="value">UP</div>
      </div>
      <div class="truck-graphic" role="img" aria-label="Illustration of a blue plow truck on the road with the blade raised and salt spreading behind"></div>
      <div class="spread-rate"><span class="value">349</span><span class="label">SPREAD<br>RATE</span></div>
      <span class="readout-label road-label">Road Temp</span>
      <div class="temp-box road-temp">70<span class="unit">F</span></div>
      <div class="brand"><span class="dot"></span>FrostLine</div>
      <div class="app-meta">FrostLine Tracker | Version: 2014-07-02 9:00</div>
      <div class="more-button">...</div>
    </div>
    <div class="action-bar"><span class="btn btn-settings">Settings</span><span class="btn btn-stop">STOP</span><span class="btn btn-quit">Quit</span></div>
    <div class="nav-column">
      <svg width="22" height="16" viewBox="0 0 22 16"><path d="M4 1h17v11M1 4h16v11H1z" fill="none" stroke="#bbb" stroke-width="1.6"/></svg>
      <svg width="22" height="16" viewBox="0 0 22 16"><path d="M2 8l9-7 9 7v7H2z" fill="none" stroke="#bbb" stroke-width="1.6"/></svg>
      <svg width="22" height="16" viewBox="0 0 22 16"><path d="M7 2L2 6l5 4M2 6h13a5 5 0 0 1 0 10H8" fill="none" stroke="#bbb" stroke-width="1.6"/></svg>
    </div>
  </div>
</div>

<!-- Night – blade down, caution -->
<div class="screen-slot thumb" style="top:284px">
  <div class="screen mode-night">
    <div class="status-bar">
      <svg width="12" height="12" viewBox="0 0 12 12"><circle cx="6" cy="6.5" r="4.5" fill="none" stroke="#33b5e5" stroke-width="1.4"/></svg>
      <svg width="14" height="12" viewBox="0 0 14 12"><path d="M1 4a9 9 0 0 1 12 0L7 11z" fill="#33b5e5"/></svg>
      <svg width="12" height="12" viewBox="0 0 12 12"><path d="M1 11h10V1z" fill="#33b5e5"/></svg>
      <svg width="7" height="12" viewBox="0 0 7 12"><rect x="0.5" y="1" width="6" height="10.5" fill="#33b5e5"/></svg>
      <span>13:37</span>
    </div>
    <div class="dashboard">
      <div class="sky"></div>
      <div class="speed-tab"></div>
      <div class="speed"><span class="label">SPEED</span><span class="value">24</span><span class="unit">MPH</span></div>
      <span class="readout-label air-label">Air Temp</span>
      <div class="temp-box air-temp">72<span class="unit">F</span></div>
      <div class="blade-state">
        <div class="label">BLADE IS</div><div class="value">DOWN</div>
        <svg width="14" height="8" viewBox="0 0 14 8"><path d="M1 1l6 6 6-6" fill="none" stroke="currentColor" stroke-width="2"/></svg>
      </div>
      <div class="truck-graphic" role="img" aria-label="Illustration of a blue plow truck on the road with the blade lowered and the spreader off"></div>
      <div class="spread-rate"><span class="value">0</span><span class="label">SPREAD<br>RATE</span></div>
      <span class="readout-label road-label">Road Temp</span>
      <div class="temp-box road-temp is-caution"><span class="caution-icon">!</span>30<span class="unit">F</span></div>
      <div class="caution-note">CAUTION</div>
      <div class="brand"><span class="dot"></span>FrostLine</div>
      <div class="app-meta">FrostLine Tracker | Version: 2014-07-02 9:00</div>
      <div class="more-button">...</div>
    </div>
    <div class="action-bar"><span class="btn btn-settings">Settings</span><span class="btn btn-stop">STOP</span><span class="btn btn-quit">Quit</span></div>
    <div class="nav-column">
      <svg width="22" height="16" viewBox="0 0 22 16"><path d="M4 1h17v11M1 4h16v11H1z" fill="none" stroke="#bbb" stroke-width="1.6"/></svg>
      <svg width="22" height="16" viewBox="0 0 22 16"><path d="M2 8l9-7 9 7v7H2z" fill="none" stroke="#bbb" stroke-width="1.6"/></svg>
      <svg width="22" height="16" viewBox="0 0 22 16"><path d="M7 2L2 6l5 4M2 6h13a5 5 0 0 1 0 10H8" fill="none" stroke="#bbb" stroke-width="1.6"/></svg>
    </div>
  </div>
</div>

<!-- Day – blade up -->
<div class="screen-slot thumb" style="top:562px">
  <div class="screen mode-day">
    <div class="status-bar">
      <svg width="12" height="12" viewBox="0 0 12 12"><circle cx="6" cy="6.5" r="4.5" fill="none" stroke="#33b5e5" stroke-width="1.4"/></svg>
      <svg width="14" height="12" viewBox="0 0 14 12"><path d="M1 4a9 9 0 0 1 12 0L7 11z" fill="#33b5e5"/></svg>
      <svg width="12" height="12" viewBox="0 0 12 12"><path d="M1 11h10V1z" fill="#33b5e5"/></svg>
      <svg width="7" height="12" viewBox="0 0 7 12"><rect x="0.5" y="1" width="6" height="10.5" fill="#33b5e5"/></svg>
      <span>13:37</span>
    </div>
    <div class="dashboard">
      <div class="sky"></div>
      <div class="speed-tab"></div>
      <div class="speed"><span class="label">SPEED</span><span class="value">24</span><span class="unit">MPH</span></div>
      <span class="readout-label air-label">Air Temp</span>
      <div class="temp-box air-temp">72<span class="unit">F</span></div>
      <div class="blade-state is-up">
        <svg width="14" height="8" viewBox="0 0 14 8"><path d="M1 7l6-6 6 6" fill="none" stroke="currentColor" stroke-width="2"/></svg>
        <div class="label">BLADE IS</div><div class="value">UP</div>
      </div>
      <div class="truck-graphic" role="img" aria-label="Illustration of a blue plow truck on a snowy road with the blade raised and salt spreading behind"></div>
      <div class="spread-rate"><span class="value">349</span><span class="label">SPREAD<br>RATE</span></div>
      <span class="readout-label road-label">Road Temp</span>
      <div class="temp-box road-temp">70<span class="unit">F</span></div>
      <div class="brand"><span class="dot"></span>FrostLine</div>
      <div class="app-meta">FrostLine Tracker | Version: 2014-07-02 9:00</div>
      <div class="more-button">...</div>
    </div>
    <div class="action-bar"><span class="btn btn-settings">Settings</span><span class="btn btn-stop">STOP</span><span class="btn btn-quit">Quit</span></div>
    <div class="nav-column">
      <svg width="22" height="16" viewBox="0 0 22 16"><path d="M4 1h17v11M1 4h16v11H1z" fill="none" stroke="#bbb" stroke-width="1.6"/></svg>
      <svg width="22" height="16" viewBox="0 0 22 16"><path d="M2 8l9-7 9 7v7H2z" fill="none" stroke="#bbb" stroke-width="1.6"/></svg>
      <svg width="22" height="16" viewBox="0 0 22 16"><path d="M7 2L2 6l5 4M2 6h13a5 5 0 0 1 0 10H8" fill="none" stroke="#bbb" stroke-width="1.6"/></svg>
    </div>
  </div>
</div>

<!-- Day – blade down, caution -->
<div class="screen-slot thumb" style="top:762px">
  <div class="screen mode-day">
    <div class="status-bar">
      <svg width="12" height="12" viewBox="0 0 12 12"><circle cx="6" cy="6.5" r="4.5" fill="none" stroke="#33b5e5" stroke-width="1.4"/></svg>
      <svg width="14" height="12" viewBox="0 0 14 12"><path d="M1 4a9 9 0 0 1 12 0L7 11z" fill="#33b5e5"/></svg>
      <svg width="12" height="12" viewBox="0 0 12 12"><path d="M1 11h10V1z" fill="#33b5e5"/></svg>
      <svg width="7" height="12" viewBox="0 0 7 12"><rect x="0.5" y="1" width="6" height="10.5" fill="#33b5e5"/></svg>
      <span>13:37</span>
    </div>
    <div class="dashboard">
      <div class="sky"></div>
      <div class="speed-tab"></div>
      <div class="speed"><span class="label">SPEED</span><span class="value">24</span><span class="unit">MPH</span></div>
      <span class="readout-label air-label">Air Temp</span>
      <div class="temp-box air-temp">72<span class="unit">F</span></div>
      <div class="blade-state">
        <div class="label">BLADE IS</div><div class="value">DOWN</div>
        <svg width="14" height="8" viewBox="0 0 14 8"><path d="M1 1l6 6 6-6" fill="none" stroke="currentColor" stroke-width="2"/></svg>
      </div>
      <div class="truck-graphic" role="img" aria-label="Illustration of a blue plow truck on a snowy road with the blade lowered and the spreader off"></div>
      <div class="spread-rate"><span class="value">0</span><span class="label">SPREAD<br>RATE</span></div>
      <span class="readout-label road-label">Road Temp</span>
      <div class="temp-box road-temp is-caution"><span class="caution-icon">!</span>30<span class="unit">F</span></div>
      <div class="caution-note">CAUTION</div>
      <div class="brand"><span class="dot"></span>FrostLine</div>
      <div class="app-meta">FrostLine Tracker | Version: 2014-07-02 9:00</div>
      <div class="more-button">...</div>
    </div>
    <div class="action-bar"><span class="btn btn-settings">Settings</span><span class="btn btn-stop">STOP</span><span class="btn btn-quit">Quit</span></div>
    <div class="nav-column">
      <svg width="22" height="16" viewBox="0 0 22 16"><path d="M4 1h17v11M1 4h16v11H1z" fill="none" stroke="#bbb" stroke-width="1.6"/></svg>
      <svg width="22" height="16" viewBox="0 0 22 16"><path d="M2 8l9-7 9 7v7H2z" fill="none" stroke="#bbb" stroke-width="1.6"/></svg>
      <svg width="22" height="16" viewBox="0 0 22 16"><path d="M7 2L2 6l5 4M2 6h13a5 5 0 0 1 0 10H8" fill="none" stroke="#bbb" stroke-width="1.6"/></svg>
    </div>
  </div>
</div>

<!-- Featured screen – night, blade down, spreading, caution -->
<div class="screen-slot hero">
  <div class="screen mode-night">
    <div class="status-bar">
      <svg width="12" height="12" viewBox="0 0 12 12"><circle cx="6" cy="6.5" r="4.5" fill="none" stroke="#33b5e5" stroke-width="1.4"/></svg>
      <svg width="14" height="12" viewBox="0 0 14 12"><path d="M1 4a9 9 0 0 1 12 0L7 11z" fill="#33b5e5"/></svg>
      <svg width="12" height="12" viewBox="0 0 12 12"><path d="M1 11h10V1z" fill="#33b5e5"/></svg>
      <svg width="7" height="12" viewBox="0 0 7 12"><rect x="0.5" y="1" width="6" height="10.5" fill="#33b5e5"/></svg>
      <span>13:37</span>
    </div>
    <div class="dashboard">
      <div class="sky"></div>
      <div class="speed-tab"></div>
      <div class="speed"><span class="label">SPEED</span><span class="value">24</span><span class="unit">MPH</span></div>
      <span class="readout-label air-label">Air Temp</span>
      <div class="temp-box air-temp">72<span class="unit">F</span></div>
      <div class="blade-state">
        <div class="label">BLADE IS</div><div class="value">DOWN</div>
        <svg width="14" height="8" viewBox="0 0 14 8"><path d="M1 1l6 6 6-6" fill="none" stroke="currentColor" stroke-width="2"/></svg>
      </div>
      <div class="truck-graphic" role="img" aria-label="Illustration of a blue plow truck on the road with the blade lowered and salt spreading behind"></div>
      <div class="spread-rate"><span class="value">349</span><span class="label">SPREAD<br>RATE</span></div>
      <span class="readout-label road-label">Road Temp</span>
      <div class="temp-box road-temp is-caution"><span class="caution-icon">!</span>30<span class="unit">F</span></div>
      <div class="caution-note">CAUTION</div>
      <div class="brand"><span class="dot"></span>FrostLine</div>
      <div class="app-meta">FrostLine Tracker | Version: 2014-07-02 9:00</div>
      <div class="more-button">...</div>
    </div>
    <div class="action-bar"><span class="btn btn-settings">Settings</span><span class="btn btn-stop">STOP</span><span class="btn btn-quit">Quit</span></div>
    <div class="nav-column">
      <svg width="22" height="16" viewBox="0 0 22 16"><path d="M4 1h17v11M1 4h16v11H1z" fill="none" stroke="#bbb" stroke-width="1.6"/></svg>
      <svg width="22" height="16" viewBox="0 0 22 16"><path d="M2 8l9-7 9 7v7H2z" fill="none" stroke="#bbb" stroke-width="1.6"/></svg>
      <svg width="22" height="16" viewBox="0 0 22 16"><path d="M7 2L2 6l5 4M2 6h13a5 5 0 0 1 0 10H8" fill="none" stroke="#bbb" stroke-width="1.6"/></svg>
    </div>
  </div>
</div>

</body>
</html>
```